An expert for Professional and Technical Evaluation of Painting Work Needs a New Letterhead Design

I own a mid-sized painting company and also work as an expert for professional and technical evaluation of painting work in the area of Zurich.

Please read the project description and the must-have-requirements carefully!

I attached 1 PDF which will help you create a new letterhead design:

THE NEW DESIGN DOESN'T NEED A LOGO! (Because it won't represent a company, it represents only a service)
Updates

Dear designers We had a discussion about the location/placement of the design and came to the conclusion that we only want the design to be in the header area of the A4-paper. We would be glad to receive some revised version of your designs. Thank you and kind regards!

Project Deadline Extended
Reason: Due to the fact that only 20% of the designer have understood the brief and submitted designs that have met the requirements we decided to extend the contest deadline.

Project Deadline Extended
Reason: A great deal of good designs were submitted in the last few days. A big thank you to all the participating designers for your good work. We need a few more days to discuss some changes with certain designers and to decide which design will win.

Target Market(s)

(Insurance) Companies, partly also private clients.

Industry/Entity Type

Painting

Colors

Designer to choose colors to be used in the design.

Requirements
Must have
• All information (text, phone numbers, ...) of the old design ("old_letterhead_design.pdf") has also to be in the new one. Additional to that there are a few changes:
The phone numbers "01 583 61 47" and "01 583 61 37" change to "044 583 61 47" and "044 583 61 37". And please mention also this email address: gutachten@valmorkeller.example .

- The design should only be in the header-area of the A4-paper. An the background color of the A4-paper will be white.

- The design should consist of two designs. One for the first page and a smaller version of the design for the following pages.

- THE NEW DESIGN DOESN'T NEED A LOGO! You can make a design with geometric forms, ...

- The new design should have a juridical look. It should only contain colors like brown, fawn, black, light green, ...... colors which look serious/reliable.
Nice to have
• Geometric Forms, Symbols or other design elements.

- It would also be nice to have some design elements which emphasize the kind of work we are offering.

```html
<!DOCTYPE html>
<html lang="de">
<head>
<meta charset="utf-8">
<title>Briefkopf – Valmor Keller</title>
<link rel="stylesheet" href="https://fonts.googleapis.com/css2?family=Raleway:wght@300;400;700&display=swap">
<style>
  :root {
    --backdrop: #b09b88;
    --paper: #ffffff;
    --brown-dark: #5e3714;
    --brown-mid: #764b29;
    --brown: #8a5c3b;
    --fawn: #a67c52;
    --umber: #3a1f10;
    --ink: #222222;
  }
  * { margin: 0; padding: 0; box-sizing: border-box; }
  html, body {
    width: 1200px; height: 1000px; overflow: hidden;
    background: var(--backdrop);
  }
  .sheet {
    position: absolute; left: 35px; top: 98px;
    width: 1131px; height: 902px;
    background: var(--paper);
  }
  .corner-accent {
    position: absolute; top: 0;
    width: 130px; height: 301px;
  }
  .corner-accent--left {
    left: 0;
    background: linear-gradient(180deg, var(--brown-dark), var(--brown), var(--brown-mid));
  }
  .corner-accent--right {
    right: 0;
    background: linear-gradient(180deg, var(--fawn), var(--brown-dark), var(--brown));
  }
  .services {
    position: absolute; left: 0; right: 0; top: 78px;
    display: flex; justify-content: center; align-items: center; gap: 7px;
    font-family: "Raleway", sans-serif; font-weight: 700; font-size: 19px;
    color: var(--ink); white-space: nowrap;
  }
  .services .sep {
    width: 9px; height: 9px; transform: rotate(45deg); margin: 0 2px;
  }
  .sep--brown { background: var(--brown); }
  .sep--dark { background: var(--brown-dark); }
  .sep--fawn { background: var(--fawn); }
  .sep--umber { background: var(--umber); }
  .contact {
    position: absolute; left: 0; right: 0; top: 174px;
    text-align: center;
    font-family: "Raleway", sans-serif; font-weight: 400; font-size: 19px;
    line-height: 23px; color: var(--ink); white-space: pre;
  }
</style>
</head>
<body>
  <div class="sheet">
    <div class="corner-accent corner-accent--left" role="img" aria-label="Eckornament aus braunen Flächen, links"></div>
    <div class="corner-accent corner-accent--right" role="img" aria-label="Eckornament aus braunen Flächen, rechts"></div>

    <div class="services">
      <span>Gutachten</span><span class="sep sep--brown"></span>
      <span>Expertisen</span><span class="sep sep--dark"></span>
      <span>Devisierungen</span><span class="sep sep--fawn"></span>
      <span>Farbberatungen</span><span class="sep sep--umber"></span>
      <span>Dekorative Gestaltungen</span>
    </div>

    <div class="contact">Valmor Keller   eidg.dipl. Malermeister   Lindenweg 7   8804 Kellbach
Telefon  044 583 61 47   Fax 044 583 61 37   Natel 079 412 56 30   gutachten@valmorkeller.example</div>
  </div>
</body>
</html>
```